Ridgefall Stoneworks Business card logo

We are a tile and natural stone installation company with an emphasis on high quality and design assistance. I prefer a black background with a graphic logo or maybe a photo that gives a feel of tile/natural stone. I like bold, but tasteful colors. Something to really catch the eye without being gaudy. The final design should convey expert quality and attention to detail.

Contact Information for Business Card

RIDGEFALL STONEWORKS Quality Design and Installation

Other font styles liked:
• Graviton, Illegal curves

Requirements
Must have
• Business card must be an eye-catcher, but tasteful.
• Information I need on the card:
• Business name and tagline
• Warren Pelsby, owner
• Phone: (xxx) xxx-xxxx
• Email
• Website

```html
<!DOCTYPE html>
<html lang="en">
<head>
<meta charset="utf-8">
<title>Ridgefall Stoneworks – Business Card</title>
<link rel="stylesheet" href="https://fonts.googleapis.com/css2?family=Mulish:wght@400;700;800&display=swap">
<style>
  :root {
    --backdrop: #d9d6d2;
    --card: #0b0b0d;
    --card-edge: #16161a;
    --ink: #ffffff;
    --ink-soft: #e6e6e6;
    --tile-blue: #4a8fd6;
  }
  * { margin: 0; padding: 0; box-sizing: border-box; }
  html, body {
    width: 1200px; height: 1000px; overflow: hidden;
    background: var(--backdrop);
    font-family: "Mulish", "Century Gothic", sans-serif;
  }
  .canvas { position: relative; width: 1200px; height: 1000px; }
  .card {
    position: absolute; left: 265px; width: 666px; height: 397px;
    background: radial-gradient(ellipse at 40% 35%, var(--card-edge), var(--card) 70%);
    color: var(--ink);
  }
  .card--front { top: 73px; }
  .card--back { top: 532px; }

  .brand {
    position: absolute; left: 40px; top: 74px; width: 256px;
    text-align: center; font-weight: 800; color: var(--ink);
  }
  .brand__square {
    width: 135px; height: 135px; margin: 0 auto 22px;
    background: var(--tile-blue);
  }
  .brand__name { display: block; line-height: 1.05; letter-spacing: 0.5px; }
  .brand__name--top { font-size: 39px; }
  .brand__name--bottom { font-size: 27px; margin-top: 6px; }

  .contact { position: absolute; left: 364px; top: 126px; }
  .contact__name { font-size: 22px; font-weight: 700; line-height: 1.2; }
  .contact__role { font-size: 17px; font-weight: 400; color: var(--ink-soft); line-height: 1.1; }
  .contact__list { list-style: none; margin-top: 38px; }
  .contact__item {
    display: flex; align-items: center; gap: 6px;
    font-size: 16.5px; line-height: 22.5px; color: var(--ink-soft);
  }
  .contact__icon { width: 12px; height: 12px; fill: var(--ink-soft); flex: none; }
</style>
</head>
<body>
<main class="canvas">

  <section class="card card--front">
    <div class="brand">
      <div class="brand__square"></div>
      <span class="brand__name brand__name--top">RIDGEFALL</span>
      <span class="brand__name brand__name--bottom">STONEWORKS</span>
    </div>
    <div class="contact">
      <p class="contact__name">Warren Pelsby</p>
      <p class="contact__role">Owner</p>
      <ul class="contact__list">
        <li class="contact__item">
          <svg class="contact__icon" viewBox="0 0 12 12"><path d="M3 0.5l1.8 2.6-1.1 1.2c.6 1.5 1.8 2.8 3.3 3.5l1.2-1.1 2.6 1.6-.8 2.4C5 10.4 1.2 6.3.8 1.4z"/></svg>
          999 999 9999
        </li>
        <li class="contact__item">
          <svg class="contact__icon" viewBox="0 0 12 12"><path d="M0 2h12v8H0z M1 3v.3l5 3.3 5-3.3V3z" fill-rule="evenodd"/></svg>
          info@ridgefallstoneworks.com
        </li>
        <li class="contact__item">
          <svg class="contact__icon" viewBox="0 0 12 12"><circle cx="6" cy="6" r="5.3" fill="none" stroke="#e6e6e6" stroke-width="1"/><ellipse cx="6" cy="6" rx="2.2" ry="5.3" fill="none" stroke="#e6e6e6" stroke-width="1"/><path d="M.8 6h10.4M1.8 3.3h8.4M1.8 8.7h8.4" stroke="#e6e6e6" stroke-width="1"/></svg>
          www.ridgefallstoneworks.com
        </li>
      </ul>
    </div>
  </section>

  <section class="card card--back">
    <div class="brand">
      <div class="brand__square"></div>
      <span class="brand__name brand__name--top">RIDGEFALL</span>
      <span class="brand__name brand__name--bottom">STONEWORKS</span>
    </div>
    <div class="contact">
      <p class="contact__name">Warren Pelsby</p>
      <p class="contact__role">Owner</p>
      <ul class="contact__list">
        <li class="contact__item">
          <svg class="contact__icon" viewBox="0 0 12 12"><path d="M3 0.5l1.8 2.6-1.1 1.2c.6 1.5 1.8 2.8 3.3 3.5l1.2-1.1 2.6 1.6-.8 2.4C5 10.4 1.2 6.3.8 1.4z"/></svg>
          999 999 9999
        </li>
        <li class="contact__item">
          <svg class="contact__icon" viewBox="0 0 12 12"><path d="M0 2h12v8H0z M1 3v.3l5 3.3 5-3.3V3z" fill-rule="evenodd"/></svg>
          info@ridgefallstoneworks.com
        </li>
        <li class="contact__item">
          <svg class="contact__icon" viewBox="0 0 12 12"><circle cx="6" cy="6" r="5.3" fill="none" stroke="#e6e6e6" stroke-width="1"/><ellipse cx="6" cy="6" rx="2.2" ry="5.3" fill="none" stroke="#e6e6e6" stroke-width="1"/><path d="M.8 6h10.4M1.8 3.3h8.4M1.8 8.7h8.4" stroke="#e6e6e6" stroke-width="1"/></svg>
          www.ridgefallstoneworks.com
        </li>
      </ul>
    </div>
  </section>

</main>
</body>
</html>
```